BW Business Card

Used Car Sales
We are trying to recreate the image of our license plate on business cards,
it is a red background with a white oval that is open on the ends
I attempted to upload the image but it was a dismal failure when the products arrived
the lettering was too small and the edges were white
I think maybe the red needs some texture in it, still red but something that doesn't look so flat
and maybe a beveled edge around the white (not sure)

Target Market(s)

Adults 25-65 that drive

Industry/Entity Type

Business

Contact Information for Business Card

Darlene Whitcombe, Sales Manager, BRIGHTWAY AUTO MART, INC., 462 Fernhill Road, Pulaski, TN 38591,
931 587-2064 (office), 931 587-6259 (fax) - We Finance everyone with approved credit
BrightwayAutoMart.Com

On Back: Financing Available - We Finance everyone with approved credit
Easy Payments: Monthly, Semi-Monthly or Weekly
Ask about our Layaway plan
Open Mon-Sat
8:30 AM - 5 PM

Requirements
Must have
• We want to match the license plate (minus holes for screws)

```html
<!DOCTYPE html>
<html lang="en">
<head>
<meta charset="utf-8">
<title>BW Business Card</title>
<link rel="stylesheet" href="https://fonts.googleapis.com/css2?family=Open+Sans:wght@400;700&display=swap">
<style>
  :root {
    --backdrop-light: #f4f4f4;
    --backdrop-dark: #d9d9d9;
    --plate-red: #ea3f4b;
    --plate-red-deep: #df2f3d;
    --oval-white: #ffffff;
    --stitch-grey: #a8a8a8;
    --ink-black: #1a1a1a;
    --ink-red: #d9303b;
  }
  html, body {
    margin: 0;
    padding: 0;
    width: 1200px;
    height: 1000px;
    overflow: hidden;
  }
  body {
    position: relative;
    background: radial-gradient(ellipse at 45% 45%, var(--backdrop-light) 0%, var(--backdrop-dark) 100%);
    font-family: "Open Sans", sans-serif;
  }
  .card {
    position: absolute;
    width: 605px;
    height: 345px;
    box-shadow: 0 1px 3px rgba(0,0,0,0.35);
    overflow: hidden;
  }
  .card--front { left: 120px; top: 171px; }
  .card--back { left: 469px; top: 565px; }
  .card__plate {
    position: absolute;
    inset: 0;
    width: 605px;
    height: 345px;
    display: block;
  }
  .card__text {
    position: absolute;
    left: 0;
    right: 0;
    text-align: center;
    margin: 0;
  }
  .holder-name {
    top: 80px;
    font-size: 26px;
    line-height: 34px;
    color: var(--ink-black);
    font-weight: 400;
  }
  .holder-name strong { font-weight: 700; }
  .holder-title {
    top: 111px;
    font-size: 19px;
    line-height: 24px;
    color: var(--ink-red);
  }
  .company-name {
    top: 146px;
    font-size: 19px;
    line-height: 26px;
    font-weight: 700;
    color: var(--ink-black);
    letter-spacing: 0.2px;
  }
  .contact-lines {
    top: 185px;
    font-size: 16.5px;
    line-height: 21.6px;
    color: var(--ink-red);
  }
  .financing-heading {
    top: 110px;
    font-size: 26px;
    line-height: 34px;
    color: var(--ink-black);
  }
  .financing-heading strong { font-weight: 700; }
  .financing-lines {
    top: 143px;
    font-size: 20px;
    line-height: 26px;
    color: var(--ink-red);
  }
</style>
</head>
<body>

<section class="card card--front" aria-label="Business card front">
  <svg class="card__plate" viewBox="0 0 605 345" aria-hidden="false">
    <defs>
      <linearGradient id="plateRedFront" x1="0" y1="0" x2="1" y2="1">
        <stop offset="0" stop-color="var(--plate-red)"/>
        <stop offset="1" stop-color="var(--plate-red-deep)"/>
      </linearGradient>
    </defs>
    <rect width="605" height="345" fill="url(#plateRedFront)" role="img" aria-label="Red textured background with faint swirl pattern"/>
    <ellipse cx="302" cy="182" rx="336" ry="137" fill="var(--oval-white)"/>
    <ellipse cx="302" cy="176" rx="332" ry="140" fill="none" stroke="var(--stitch-grey)" stroke-width="1" stroke-dasharray="4 3"/>
    <ellipse cx="302" cy="186" rx="324" ry="126" fill="none" stroke="var(--stitch-grey)" stroke-width="1" stroke-dasharray="4 3"/>
  </svg>
  <p class="card__text holder-name">Darlene <strong>Whitcombe</strong></p>
  <p class="card__text holder-title">Sales Manager</p>
  <p class="card__text company-name">BRIGHTWAY AUTO MART, INC.</p>
  <p class="card__text contact-lines">
    462 Fernhill Road, Pulaski, TN 38591,<br>
    931 587-2064 (office),<br>
    931 587-6259 (fax) -<br>
    We Finance everyone with approved credit<br>
    BrightwayAutoMart.Com
  </p>
</section>

<section class="card card--back" aria-label="Business card back">
  <svg class="card__plate" viewBox="0 0 605 345" aria-hidden="false">
    <defs>
      <linearGradient id="plateRedBack" x1="0" y1="0" x2="1" y2="1">
        <stop offset="0" stop-color="var(--plate-red)"/>
        <stop offset="1" stop-color="var(--plate-red-deep)"/>
      </linearGradient>
    </defs>
    <rect width="605" height="345" fill="url(#plateRedBack)" role="img" aria-label="Red textured background with faint swirl pattern"/>
    <ellipse cx="302" cy="182" rx="336" ry="137" fill="var(--oval-white)"/>
    <ellipse cx="302" cy="176" rx="332" ry="140" fill="none" stroke="var(--stitch-grey)" stroke-width="1" stroke-dasharray="4 3"/>
    <ellipse cx="302" cy="186" rx="324" ry="126" fill="none" stroke="var(--stitch-grey)" stroke-width="1" stroke-dasharray="4 3"/>
  </svg>
  <p class="card__text financing-heading">-: Financing <strong>Available</strong> :-</p>
  <p class="card__text financing-lines">
    We Finance everyone with approved credit<br>
    Easy Payments: Monthly, Semi-Monthly or<br>
    Weekly Ask about our Layaway plan<br>
    Open Mon-Sat 8:30 AM - 5 PM
  </p>
</section>

</body>
</html>
```